Medical IT Business with New logo needs a fresh stationary design

First time on sketch Harbor; Thought I would give it a go.
This project is for business cards alone but we have loads of design work that needs to take place in the immediate future.

We provide IT services to the Medical Industry and value ourselves as offering a premium product to the market.

I am after a fresh, clean design using full colour 2 sided cards which includes our current colour palettes from our logo.

Card's must include:
- Logo
- Slogan
- Name
- Adress
- Email
- Phone
- Fax
- Mobile

Target Market(s)

Surgeons, High Profile Medical Personnel

Industry/Entity Type

Business

Fonts, CMYK Colours and Logo files attached.

Requirements
Must have
• Card's must include:
• - Logo
• - Slogan
• - Name
• - Adress
• - Email
• - Phone
• - Fax
• - Mobile
Nice to have
• Needs to incorporate our colour palette (attached CMYK colours)
Should not have
• Black backgrounds. Black text ok.

```html
<!DOCTYPE html>
<html lang="en">
<head>
<meta charset="utf-8">
<title>Carewave Systems – Business Card</title>
<link rel="stylesheet" href="https://fonts.googleapis.com/css2?family=Arimo:wght@400;700&family=Open+Sans:wght@400;600&display=swap">
<style>
  :root {
    --navy: #0f3569;
    --navy-deep: #0a2a57;
    --blue: #1b78b8;
    --sky: #2a8cc8;
    --text: #2b2b2b;
    --grey: #6c7a86;
    --paper: #ffffff;
    --stage: #e9ecef;
  }
  * { box-sizing: border-box; margin: 0; padding: 0; }
  html, body { width: 1200px; height: 950px; overflow: hidden; }
  body {
    background: var(--stage);
    font-family: "Arimo", Arial, sans-serif;
    position: relative;
  }
  .card {
    position: absolute;
    left: 250px;
    width: 700px;
    height: 400px;
    overflow: hidden;
    box-shadow: 0 6px 18px rgba(0,0,0,.12);
  }
  /* ---------- front ---------- */
  .card-front { top: 45px; background: var(--paper); }
  .holder { position: absolute; left: 40px; top: 70px; }
  .holder-name { font-size: 30px; font-weight: 700; color: var(--navy); }
  .holder-role { font-size: 21px; color: var(--blue); margin-top: 2px; }
  .rule-short {
    position: absolute; left: 40px; top: 142px; width: 230px;
    border-top: 1.5px solid var(--blue);
  }
  .rule-long {
    position: absolute; left: 270px; top: 142px; width: 380px;
    border-top: 1.5px solid var(--blue);
    transform-origin: left; transform: translateY(0);
  }
  .contacts { position: absolute; left: 40px; top: 160px; list-style: none; }
  .contacts li {
    display: flex; align-items: center; gap: 12px;
    font-size: 21px; color: var(--text); height: 30px;
  }
  .contacts svg { width: 20px; height: 20px; fill: var(--navy); flex: none; }
  .brand { position: absolute; right: 40px; top: 62px; display: flex; align-items: center; gap: 14px; }
  .brand-dot { width: 78px; height: 78px; border-radius: 50%; background: var(--blue); flex: none; }
  .brand-text { line-height: 1; }
  .brand-name { font-size: 30px; font-weight: 700; color: var(--navy); letter-spacing: .5px; }
  .brand-slogan {
    font-family: "Open Sans", Arial, sans-serif; font-size: 15px;
    color: var(--sky); margin-top: 6px;
  }
  .address {
    position: absolute; right: 50px; top: 250px; text-align: right;
    font-size: 21px; color: var(--text); line-height: 1.35;
  }
  .band { position: absolute; left: 0; bottom: 0; width: 700px; height: 40px; }
  /* ---------- back ---------- */
  .card-back {
    top: 505px;
    background: linear-gradient(120deg, var(--navy-deep) 0%, var(--navy) 60%, #1d4a82 100%);
  }
  .back-disc {
    position: absolute; left: 50%; top: 95px; width: 180px; height: 180px;
    margin-left: -90px; border-radius: 50%; background: #e8ecf1;
  }
  .back-web {
    position: absolute; left: 0; right: 0; top: 300px; text-align: center;
    font-size: 20px; color: #e8ecf1; letter-spacing: 2px;
  }
</style>
</head>
<body>

<section class="card card-front" aria-label="Business card, front">
  <div class="holder">
    <p class="holder-name">Nora Vance</p>
    <p class="holder-role">President</p>
  </div>
  <div class="rule-short"></div>
  <div class="rule-long"></div>

  <ul class="contacts">
    <li>
      <svg viewBox="0 0 24 24" aria-label="Phone"><path d="M6.6 10.8a15.2 15.2 0 0 0 6.6 6.6l2.2-2.2a1 1 0 0 1 1-.25 11.4 11.4 0 0 0 3.6.57 1 1 0 0 1 1 1V20a1 1 0 0 1-1 1A17 17 0 0 1 3 4a1 1 0 0 1 1-1h3.5a1 1 0 0 1 1 1c0 1.25.2 2.45.57 3.57a1 1 0 0 1-.25 1z"/></svg>
      555 0142 7781
    </li>
    <li>
      <svg viewBox="0 0 24 24" aria-label="Mobile"><path d="M7 1h10a2 2 0 0 1 2 2v18a2 2 0 0 1-2 2H7a2 2 0 0 1-2-2V3a2 2 0 0 1 2-2zm0 3v14h10V4zm5 15.5a1 1 0 1 0 0 2 1 1 0 0 0 0-2z"/></svg>
      555 0198 3364
    </li>
    <li>
      <svg viewBox="0 0 24 24" aria-label="Fax"><path d="M7 2h8l3 3v5H7zM4 11h16a2 2 0 0 1 2 2v7a2 2 0 0 1-2 2H4a2 2 0 0 1-2-2v-7a2 2 0 0 1 2-2zm3 3v2h10v-2z"/></svg>
      555 0127 4490
    </li>
    <li>
      <svg viewBox="0 0 24 24" aria-label="Email"><path d="M2 5h20v14H2zm2 2v.5l8 5.5 8-5.5V7z"/></svg>
      nora@carewave.net
    </li>
  </ul>

  <div class="brand">
    <span class="brand-dot"></span>
    <div class="brand-text">
      <p class="brand-name">CAREWAVE SYSTEMS</p>
      <p class="brand-slogan">always with your clinic</p>
    </div>
  </div>

  <address class="address" style="font-style:normal">
    2710 Larkspur Avenue<br>
    Maple Ridge, OR 97000<br>
    www.carewave.net
  </address>

  <svg class="band" viewBox="0 0 700 40" preserveAspectRatio="none" aria-hidden="true">
    <polygon points="0,12 430,12 446,40 0,40" fill="var(--navy)"/>
    <polygon points="430,24 700,24 700,40 440,40" fill="var(--sky)"/>
  </svg>
</section>

<section class="card card-back" aria-label="Business card, back">
  <div class="back-disc"></div>
  <p class="back-web">www.carewave.net</p>
</section>

</body>
</html>
```